Luxury Business Card Design

We need a business card design for a law firm that look sophisticated and luxury

Target Market(s)

Australian legal markets

Industry/Entity Type

Legal

Contact Information for Business Card

Attached

Requirements
Must have
• Logo, head office address on front side and 2 other addresses on the back side.
Nice to have
• Please see below our current business card. Need something more sophisticated and luxury feel

```html
<!DOCTYPE html>
<html lang="en">
<head>
<meta charset="utf-8">
<title>Ashcombe Lawyers – Business Card</title>
<link href="https://fonts.googleapis.com/css2?family=Cinzel:wght@600&family=Montserrat:wght@400;700&display=swap" rel="stylesheet">
<style>
  :root {
    --bg: #3a3a3a;
    --forest: #011a12;
    --gold: #d4ac5e;
    --paper: #ffffff;
    --ink: #111111;
  }
  * { margin: 0; padding: 0; box-sizing: border-box; }
  html, body { width: 1200px; height: 1200px; overflow: hidden; }
  body {
    background: var(--bg);
    font-family: "Montserrat", sans-serif;
    position: relative;
  }
  .card {
    position: absolute;
    left: 250px;
    width: 700px;
    height: 400px;
    border-radius: 22px;
    overflow: hidden;
    box-shadow: 0 14px 30px rgba(0,0,0,0.45);
  }
  .card-back { top: 130px; background: var(--forest); }
  .card-front { top: 640px; background: var(--paper); }

  .brand {
    display: flex;
    flex-direction: column;
    align-items: center;
  }
  .brand-circle {
    width: 96px; height: 96px;
    border: 6px solid var(--gold);
    border-radius: 50%;
  }
  .brand-name {
    font-family: "Cinzel", serif;
    font-weight: 600;
    text-align: center;
    line-height: 1.1;
  }
  .card-back .brand {
    position: absolute; left: 0; right: 0; top: 90px;
  }
  .card-back .brand-name {
    color: var(--paper);
    font-size: 52px;
    margin-top: 30px;
    letter-spacing: 2px;
  }

  .card-front .wave { position: absolute; inset: 0; }
  .card-front .brand {
    position: absolute; left: 40px; top: 42px; width: 300px;
  }
  .card-front .brand-circle { width: 70px; height: 70px; border-width: 4px; }
  .card-front .brand-name {
    color: var(--forest);
    font-size: 30px;
    margin-top: 14px;
  }
  .address {
    position: absolute; left: 64px; top: 212px;
    font-size: 15px; color: var(--ink); line-height: 1.4;
  }
  .person {
    position: absolute; right: 40px; top: 40px; text-align: right;
  }
  .person-name { color: var(--gold); font-weight: 700; font-size: 24px; }
  .person-role { color: var(--ink); font-size: 13px; line-height: 1.45; margin-top: 2px; }

  .contacts {
    position: absolute; right: 28px; top: 190px;
    list-style: none; color: var(--paper); font-size: 13px;
  }
  .contacts li {
    display: flex; justify-content: flex-end; align-items: center;
    gap: 10px; height: 28px;
  }
  .contacts svg { width: 16px; height: 16px; fill: var(--gold); flex: none; }
</style>
</head>
<body>

<section class="card card-back">
  <div class="brand">
    <div class="brand-circle"></div>
    <div class="brand-name">ASHCOMBE LAWYERS</div>
  </div>
</section>

<section class="card card-front">
  <svg class="wave" viewBox="0 0 700 400" preserveAspectRatio="none" aria-hidden="true">
    <path d="M0,318 C150,410 300,390 390,270 C470,165 580,110 700,100 L700,400 L0,400 Z" fill="var(--forest)"/>
    <path d="M40,330 C180,395 300,378 380,278 C455,185 550,130 640,108" fill="none" stroke="var(--paper)" stroke-width="5"/>
    <path d="M80,300 C170,362 270,350 335,288 C270,330 180,338 80,300 Z" fill="var(--gold)"/>
  </svg>

  <div class="brand">
    <div class="brand-circle"></div>
    <div class="brand-name">ASHCOMBE LAWYERS</div>
  </div>

  <p class="address">Ashcombe House, 42 Harbour Terrace<br>Kelvin Grove. qld 4059</p>

  <div class="person">
    <p class="person-name">Daniel Marsh</p>
    <p class="person-role">Director &amp; Principal Solicitor<br>MBA, Juris Doctor</p>
  </div>

  <ul class="contacts">
    <li>+61 7 3000 4812
      <svg viewBox="0 0 24 24"><path d="M6.6 10.8a15 15 0 0 0 6.6 6.6l2.2-2.2a1 1 0 0 1 1-.25 11.4 11.4 0 0 0 3.6.6 1 1 0 0 1 1 1V20a1 1 0 0 1-1 1A17 17 0 0 1 3 4a1 1 0 0 1 1-1h3.5a1 1 0 0 1 1 1c0 1.25.2 2.45.57 3.57a1 1 0 0 1-.25 1z"/></svg></li>
    <li>+61 0400 123 987
      <svg viewBox="0 0 24 24"><path d="M7 1h10a2 2 0 0 1 2 2v18a2 2 0 0 1-2 2H7a2 2 0 0 1-2-2V3a2 2 0 0 1 2-2zm0 3v14h10V4zm5 15.5a1 1 0 1 0 0 2 1 1 0 0 0 0-2z"/></svg></li>
    <li>daniel@ashcombelawyers.com.au
      <svg viewBox="0 0 24 24"><path d="M2 5h20v14H2zm2 2v.4l8 5.1 8-5.1V7z"/></svg></li>
    <li>www.ashcombelawyers.com.au
      <svg viewBox="0 0 24 24"><path d="M12 2a10 10 0 1 0 0 20 10 10 0 0 0 0-20zm6.9 6h-2.9a15 15 0 0 0-1.4-3.6A8 8 0 0 1 18.9 8zM12 4c.8 1.2 1.5 2.5 1.9 4h-3.8c.4-1.5 1.1-2.8 1.900-4zM4.3 14a8 8 0 0 1 0-4h3.4a16 16 0 0 0 0 4zm.8 2h2.9c.3 1.3.8 2.5 1.4 3.6A8 8 0 0 1 5.1 16zM8 8H5.1a8 8 0 0 1 4.3-3.6C8.8 5.5 8.3 6.7 8 8zm4 12c-.8-1.2-1.5-2.5-1.9-4h3.8c-.4 1.5-1.1 2.8-1.9 4zm2.3-6H9.7a14 14 0 0 1 0-4h4.6a14 14 0 0 1 0 4zm.3 5.6c.6-1.1 1.1-2.3 1.4-3.6h2.9a8 8 0 0 1-4.3 3.6zM16.3 14a16 16 0 0 0 0-4h3.4a8 8 0 0 1 0 4z"/></svg></li>
  </ul>
</section>

</body>
</html>
```